Yoga for Scoliosis business card/logo design

I need a business card/logo design for my new business. I am a registered yoga teacher and am certified in yoga for scoliosis. I'd like my card to read "Marlow Yoga Yoga for a Healthy Spine" and would like to incorporate one of the letters in my name{ ie the first vertical line of the letter " H "or "D"} to resemble a scoliotic spine. I regularly teach the following:Yoga for Scoliosis, Yoga for Back Health, Hatha yoga, Vinyasa yoga with Iyengar style alignment. This business is mostly for private clients, but I also teach group, semi-private & work shop classes. I like the colors green (light emerald) and royal blue. I'd like the design to be somewhat sleek, but not too modern. I also like the idea of a ying/yang symbol with a scoliotic spine dviding it.

Danielle Marlow
200 RYT, Certified Yoga for Scoliosis Instructor
MarlowYoga.example
MarlowYoga@mailbox.example
555-412-3097

```html
<!DOCTYPE html>
<html lang="en">
<head>
<meta charset="utf-8">
<title>Marlow Yoga — Business Card</title>
<link rel="stylesheet" href="https://fonts.googleapis.com/css2?family=Open+Sans:wght@400;600;700&display=swap">
<style>
  :root {
    --royal: #123d8c;
    --royal-deep: #0b2a6b;
    --royal-light: #2150a8;
    --emerald: #33c4b0;
    --paper: #ffffff;
    --stage: #eceae6;
    --ink-soft: #dbe6f7;
  }
  * { box-sizing: border-box; margin: 0; padding: 0; }
  html, body {
    width: 1200px; height: 1023px; overflow: hidden;
    background: var(--stage);
    font-family: "Open Sans", Arial, sans-serif;
  }
  .canvas { position: relative; width: 1200px; height: 1023px; }

  .card {
    position: absolute; width: 540px; height: 309px;
    border-radius: 4px; overflow: hidden;
    box-shadow: 0 10px 30px rgba(0,0,0,.18);
  }
  .card-front { left: 70px; top: 170px; background: var(--paper); }
  .card-back {
    left: 600px; top: 540px;
    background: linear-gradient(135deg, var(--royal-light) 0%, var(--royal) 45%, var(--royal-deep) 100%);
  }

  .front-wave { position: absolute; inset: 0; }

  .brand { position: absolute; display: flex; align-items: center; gap: 14px; }
  .brand-dot { border-radius: 50%; flex: none; }
  .brand-name { font-weight: 600; white-space: nowrap; letter-spacing: .5px; }

  .card-front .brand { left: 30px; top: 200px; }
  .card-front .brand-dot { width: 64px; height: 64px; background: var(--royal); }
  .card-front .brand-name { font-size: 30px; color: var(--royal); }

  .card-back .brand { left: 50%; top: 50%; transform: translate(-50%, -50%); }
  .card-back .brand-dot { width: 66px; height: 66px; background: var(--paper); }
  .card-back .brand-name { font-size: 36px; color: var(--paper); }

  .contact-block {
    position: absolute; right: 30px; top: 26px; text-align: right;
  }
  .holder-name { font-size: 21px; font-weight: 700; color: var(--paper); }
  .holder-title { font-size: 13px; color: var(--emerald); margin-top: 2px; }
  .contact-list { list-style: none; margin-top: 16px; }
  .contact-list li {
    display: flex; justify-content: flex-end; align-items: center; gap: 8px;
    font-size: 12.5px; color: var(--ink-soft); line-height: 21px;
  }
  .contact-list svg { width: 13px; height: 13px; flex: none; }
</style>
</head>
<body>
<main class="canvas">

  <section class="card card-front" aria-label="Business card front">
    <svg class="front-wave" viewBox="0 0 540 309" preserveAspectRatio="none" aria-hidden="true">
      <path d="M120 0 C 200 30, 250 150, 380 240 C 440 280, 500 295, 540 302 L540 0 Z" fill="var(--royal)"/>
      <path d="M120 0 C 200 30, 250 150, 380 240 C 440 280, 500 295, 540 302" fill="none" stroke="var(--emerald)" stroke-width="6"/>
    </svg>

    <div class="brand">
      <span class="brand-dot"></span>
      <span class="brand-name">Marlow Yoga</span>
    </div>

    <div class="contact-block">
      <p class="holder-name">Danielle Marlow 200 RYT</p>
      <p class="holder-title">Certified Yoga for Scoliosis Instructor</p>
      <ul class="contact-list">
        <li>555-412-3097
          <svg viewBox="0 0 16 16"><rect width="16" height="16" rx="3" fill="var(--emerald)"/><path d="M5 3.5l2 2-1 1.5c.7 1.4 1.6 2.3 3 3l1.5-1 2 2-1.2 1.5C7.5 12 4 8.5 3.5 4.7z" fill="var(--royal)"/></svg>
        </li>
        <li>www.MarlowYoga.example
          <svg viewBox="0 0 16 16"><rect width="16" height="16" rx="3" fill="var(--emerald)"/><circle cx="8" cy="8" r="4.5" fill="none" stroke="var(--royal)" stroke-width="1.3"/><path d="M3.5 8h9M8 3.5v9" stroke="var(--royal)" stroke-width="1.1"/></svg>
        </li>
        <li>MarlowYoga@mailbox.example
          <svg viewBox="0 0 16 16"><rect width="16" height="16" rx="3" fill="var(--emerald)"/><rect x="3" y="4.5" width="10" height="7" fill="none" stroke="var(--royal)" stroke-width="1.3"/><path d="M3 4.5l5 4 5-4" fill="none" stroke="var(--royal)" stroke-width="1.3"/></svg>
        </li>
      </ul>
    </div>
  </section>

  <section class="card card-back" aria-label="Business card back">
    <div class="brand">
      <span class="brand-dot"></span>
      <span class="brand-name">Marlow Yoga</span>
    </div>
  </section>

</main>
</body>
</html>
```